Business Card and Stationary Design for Solstice Land Company
Solstice Land Partners
Business Card and Stationary Design for Solstice Land Company - Real Estate
Creative Brief
Use same font as used in my logo
Tobias "TK" Kalder
Realtor
2876 Mellow Crest Lane Irvine, CA 92611
tk@TheSolsticeLP.example
www.TheSolsticeLP.example
BRE Lic: 07326159
We need the following design work done: Business Cards, Presentation Folder, Letterhead, Envelopes. We will upload our logo and the design templates from our print shop for all the above items needed in order to print correctly. Business Cards (Front & Back): 4 color both sides. Presentation Folder - (Front, Back and inside) 4 colors all sides, including business card slit inside.
We will upload pictures of sample business cards (Front and Back) that we like from competitor companies.

```html
<!DOCTYPE html>
<html lang="en">
<head>
<meta charset="utf-8">
<title>Solstice Land Partners – Business Card</title>
<link rel="stylesheet" href="https://fonts.googleapis.com/css2?family=Poppins:wght@600&family=Montserrat:wght@400;600&display=swap">
<style>
  :root {
    --page-bg: #6b6866;
    --card-white: #ffffff;
    --card-black: #121212;
    --accent-orange: #f15a22;
    --text-light: #f2f2f2;
    --text-muted: #b5b5b5;
    --brand-dark: #1d1d1d;
  }
  html, body {
    margin: 0;
    width: 1200px;
    height: 899px;
    overflow: hidden;
    background: var(--page-bg);
  }
  .canvas {
    position: relative;
    width: 1200px;
    height: 899px;
  }
  .card {
    position: absolute;
    width: 640px;
    height: 366px;
    border-radius: 26px;
    overflow: hidden;
    background: var(--card-white);
    box-shadow: 0 10px 30px rgba(0,0,0,0.35);
  }
  .card-front { left: 90px; top: 110px; }
  .card-back  { left: 470px; top: 440px; }

  .card-shape {
    position: absolute;
    inset: 0;
    width: 100%;
    height: 100%;
  }
  .contact-block {
    position: absolute;
    left: 40px;
    top: 52px;
    width: 250px;
    font-family: "Montserrat", sans-serif;
    color: var(--text-light);
  }
  .holder-name {
    margin: 0;
    font-size: 19px;
    font-weight: 600;
    letter-spacing: 1px;
  }
  .holder-role {
    margin: 4px 0 0;
    font-size: 12px;
    color: var(--text-muted);
  }
  .holder-address {
    margin: 40px 0 0;
    font-size: 11.5px;
    line-height: 1.6;
  }
  .contact-list {
    list-style: none;
    margin: 30px 0 0;
    padding: 0;
    font-size: 11.5px;
    line-height: 1.9;
  }
  .contact-list li {
    display: flex;
    align-items: center;
    gap: 8px;
  }
  .contact-icon {
    width: 10px;
    height: 10px;
    fill: var(--text-light);
  }

  .brand {
    position: absolute;
    display: flex;
    align-items: center;
    gap: 10px;
    font-family: "Poppins", sans-serif;
    font-weight: 600;
    color: var(--brand-dark);
    white-space: nowrap;
  }
  .brand-square {
    width: 22px;
    height: 22px;
    background: var(--accent-orange);
  }
  .card-front .brand {
    right: 34px;
    top: 150px;
    font-size: 25px;
  }
  .card-back .brand {
    left: 50%;
    top: 50%;
    transform: translate(-50%, -50%);
    font-size: 34px;
  }
  .card-back .brand-square { width: 28px; height: 28px; }
</style>
</head>
<body>
<main class="canvas">

  <section class="card card-front" aria-label="Business card front">
    <svg class="card-shape" viewBox="0 0 640 366" preserveAspectRatio="none" aria-hidden="true">
      <path d="M0 0 H300 C250 120 260 250 340 366 H0 Z" fill="var(--card-black)"/>
      <path d="M300 0 C250 120 260 250 340 366 H356 C274 250 264 120 316 0 Z" fill="var(--accent-orange)"/>
    </svg>

    <div class="contact-block">
      <h1 class="holder-name">TOBIAS KALDER</h1>
      <p class="holder-role">Realtor</p>
      <p class="holder-address">2876 Mellow Crest Lane<br>Irvine, CA 92611</p>
      <ul class="contact-list">
        <li>
          <svg class="contact-icon" viewBox="0 0 10 10"><path d="M2 0 L4 2.5 L3 3.8 C3.8 5.4 4.6 6.2 6.2 7 L7.5 6 L10 8 L8.5 10 C4 9.5 0.5 6 0 1.5 Z"/></svg>
          014 552 0318
        </li>
        <li>
          <svg class="contact-icon" viewBox="0 0 10 10"><rect x="2" y="0" width="6" height="10" rx="1"/></svg>
          014 552 0319
        </li>
        <li>
          <svg class="contact-icon" viewBox="0 0 10 10"><path d="M0 2 H10 V8 H0 Z M0 2 L5 6 L10 2" stroke="var(--card-black)" stroke-width="0.8"/></svg>
          tk@solsticelp.example
        </li>
        <li>
          <svg class="contact-icon" viewBox="0 0 10 10"><circle cx="5" cy="5" r="5"/></svg>
          www.solsticelp.example
        </li>
      </ul>
    </div>

    <div class="brand">
      <span class="brand-square" aria-hidden="true"></span>
      <span class="brand-name">Solstice Land Partners</span>
    </div>
  </section>

  <section class="card card-back" aria-label="Business card back">
    <div class="brand">
      <span class="brand-square" aria-hidden="true"></span>
      <span class="brand-name">Solstice Land Partners</span>
    </div>
  </section>

</main>
</body>
</html>
```